Roof Plumbing Company needs simple, modern business card using the attached logo and below details:

Dean Halloway
Summit Gutters Pty Ltd
ABN: 58 214 937 062
Phone: 0417 286 531
Email: summitgutters@mailbrook.com
Website: summitgutters.com.au

For all of your metal roof plumbing requirements contact Summit Gutters for an obligation free quote - no job too big or to small!

Industry/Entity Type

Business

Contact Information for Business Card

Dean Halloway
Summit Gutters Pty Ltd
ABN 58 214 937 062
0417 286 531
summitgutters@mailbrook.com
summitgutters.com.au

Requirements
Must have
• Bright eye catching design, professional look

```html
<!DOCTYPE html>
<html lang="en">
<head>
<meta charset="utf-8">
<title>Summit Gutters – Business Card</title>
<link rel="stylesheet" href="https://fonts.googleapis.com/css2?family=Nunito+Sans:wght@400;800&display=swap">
<style>
  :root {
    --page-bg: #ececec;
    --card-bg: #ffffff;
    --brand-red: #c8161d;
    --brand-red-light: #e0262c;
    --brand-red-dark: #a80f15;
    --ink: #2b2b2b;
    --on-red: #ffffff;
  }
  * { margin: 0; padding: 0; box-sizing: border-box; }
  html, body {
    width: 1200px; height: 1000px; overflow: hidden;
    background: var(--page-bg);
    font-family: "Nunito Sans", Arial, sans-serif;
  }
  .business-card {
    position: absolute; left: 100px; top: 202px;
    width: 1000px; height: 596px;
    background: var(--card-bg);
    box-shadow: 0 6px 18px rgba(0,0,0,0.18);
    overflow: hidden;
  }
  .brand-name {
    position: absolute; left: 50px; top: 200px; width: 460px;
    color: var(--brand-red);
    font-weight: 800; font-size: 44px; line-height: 1.1;
    letter-spacing: 1px; text-transform: uppercase;
    text-align: center;
  }
  .contact-block { position: absolute; left: 575px; top: 128px; }
  .contact-name {
    color: var(--brand-red); font-weight: 800; font-size: 37px;
    letter-spacing: 0.5px; text-transform: uppercase;
    margin-bottom: 40px;
  }
  .contact-line {
    display: flex; align-items: center; gap: 10px;
    color: var(--ink); font-size: 26px; font-weight: 400;
    height: 38px;
  }
  .contact-line svg { width: 22px; height: 22px; fill: var(--brand-red); flex: none; }
  .contact-line.abn { margin-bottom: 6px; }
  .tagline-band {
    position: absolute; left: 0; right: 0; top: 466px; height: 100px;
    background: linear-gradient(90deg, var(--brand-red-dark), var(--brand-red-light) 50%, var(--brand-red-dark));
    color: var(--on-red);
    display: flex; align-items: center; justify-content: center;
    text-align: center; font-size: 25px; line-height: 1.4;
    padding: 0 40px;
  }
</style>
</head>
<body>
  <div class="business-card">
    <div class="brand-name">Summit Gutters<br>Pty Ltd</div>

    <div class="contact-block">
      <div class="contact-name">Dean Halloway</div>
      <div class="contact-line abn">ABN 58 214 937 062</div>
      <div class="contact-line">
        <svg viewBox="0 0 24 24" aria-hidden="true"><path d="M6.6 10.8a15.1 15.1 0 0 0 6.6 6.6l2.2-2.2c.3-.3.7-.4 1-.2 1.1.4 2.3.6 3.6.6.6 0 1 .4 1 1V20c0 .6-.4 1-1 1A17 17 0 0 1 3 4c0-.6.4-1 1-1h3.5c.6 0 1 .4 1 1 0 1.3.2 2.5.6 3.6.1.3 0 .7-.2 1z"/></svg>
        0417 286 531
      </div>
      <div class="contact-line">
        <svg viewBox="0 0 24 24" aria-hidden="true"><path d="M2 5h20v14H2zm2 2v.5l8 5 8-5V7zm0 3v7h16v-7l-8 5z"/></svg>
        summitgutters@mailbrook.com
      </div>
      <div class="contact-line">
        <svg viewBox="0 0 24 24" aria-hidden="true"><path d="M12 2a10 10 0 1 0 0 20 10 10 0 0 0 0-20zm6.9 6h-3a15 15 0 0 0-1.3-3.9A8 8 0 0 1 18.9 8zM12 4c.8 1.2 1.5 2.5 1.9 4h-3.8c.4-1.5 1.1-2.8 1.9-4zM4.3 14a8 8 0 0 1 0-4h3.4a16 16 0 0 0 0 4zm.8 2h3a15 15 0 0 0 1.3 3.9A8 8 0 0 1 5.1 16zm3-8h-3a8 8 0 0 1 4.3-3.9C8.8 5.3 8.4 6.6 8.1 8zM12 20c-.8-1.2-1.5-2.5-1.9-4h3.8c-.4 1.5-1.1 2.8-1.9 4zm2.3-6H9.7a14 14 0 0 1 0-4h4.6a14 14 0 0 1 0 4zm.3 5.9c.6-1.2 1-2.5 1.3-3.9h3a8 8 0 0 1-4.3 3.9zm1.7-5.9a16 16 0 0 0 0-4h3.4a8 8 0 0 1 0 4z"/></svg>
        summitgutters.com.au
      </div>
    </div>

    <div class="tagline-band">
      For all of your metal roof plumbing requirements contact Summit Gutters for<br>an obligation free quote - no job too big or to small!
    </div>
  </div>
</body>
</html>
```